We need a business card design for Corvana Group. We are a healthcare recruiting, wellness and education company. We partner with medical facilities to find quality candidates. We also offer free wellness courses.
The final design should communicate an emphasis on recruiting and wellness
The main purpose of the business card is to utilized it for networking events, give to hospitals, executives, VCs surgery centers and clinics. I want it to be sleek, clean, use of our brand colors and professional.

```html
<!DOCTYPE html>
<html lang="en">
<head>
<meta charset="utf-8">
<title>Corvana Group – Business Card</title>
<link href="https://fonts.googleapis.com/css2?family=Montserrat:wght@400;500;700&display=swap" rel="stylesheet">
<style>
  :root {
    --brand-green: #035e52;
    --card-white: #f3f3f2;
    --ink: #1f2a28;
    --backdrop: #1d1d1d;
  }
  * { margin: 0; padding: 0; box-sizing: border-box; }
  html, body {
    width: 1200px; height: 1059px; overflow: hidden;
    background: var(--backdrop);
    font-family: "Montserrat", sans-serif;
  }
  .card {
    position: absolute; left: 255px;
    width: 690px; height: 392px;
    border-radius: 18px;
  }
  .card--front { top: 89px; background: var(--card-white); color: var(--ink); }
  .card--back { top: 547px; background: var(--brand-green); color: #fff; }

  .brand { position: absolute; left: 0; right: 0; display: flex; align-items: center; justify-content: center; gap: 16px; }
  .brand__mark { display: block; border-radius: 6px; }
  .brand__name { font-weight: 500; letter-spacing: -0.5px; line-height: 1; }

  .card--front .brand { top: 66px; }
  .card--front .brand__mark { width: 44px; height: 44px; background: var(--brand-green); }
  .card--front .brand__name { font-size: 42px; color: var(--brand-green); }

  .card--back .brand { top: 160px; gap: 22px; }
  .card--back .brand__mark { width: 62px; height: 62px; background: #fff; border-radius: 8px; }
  .card--back .brand__name { font-size: 58px; color: #fff; }

  .person { position: absolute; top: 183px; left: 0; right: 0; text-align: center; }
  .person__name { font-size: 24px; font-weight: 700; letter-spacing: 1px; color: var(--brand-green); line-height: 1.1; }
  .person__role { font-size: 15px; font-weight: 400; letter-spacing: 0.6px; color: var(--ink); margin-top: 2px; }

  .divider { position: absolute; top: 240px; left: 38px; right: 38px; height: 1px; background: var(--brand-green); }

  .contact { position: absolute; top: 258px; left: 38px; list-style: none; }
  .contact__item { display: flex; align-items: center; gap: 10px; font-size: 16px; letter-spacing: 0.5px; height: 25.3px; }
  .contact__icon { width: 12px; height: 12px; fill: var(--brand-green); flex: none; }

  .address { position: absolute; right: 38px; top: 309px; text-align: right; font-size: 16px; letter-spacing: 0.5px; line-height: 25.3px; font-style: normal; }

  .site { position: absolute; top: 339px; left: 0; right: 0; text-align: center; font-size: 16px; letter-spacing: 2px; font-weight: 400; }
  .site strong { font-weight: 700; }
</style>
</head>
<body>
  <section class="card card--front">
    <div class="brand">
      <span class="brand__mark"></span>
      <span class="brand__name">Corvana Group</span>
    </div>
    <div class="person">
      <div class="person__name">DANIEL RESTREPO</div>
      <div class="person__role">Owner &amp; Manager</div>
    </div>
    <div class="divider"></div>
    <ul class="contact">
      <li class="contact__item">
        <svg class="contact__icon" viewBox="0 0 12 12"><path d="M1 4c0-2 10-2 10 0v1H8V4H4v1H1zM3 6h6l2 4H1z"/></svg>
        555 214 7730
      </li>
      <li class="contact__item">
        <svg class="contact__icon" viewBox="0 0 12 12"><path d="M3 0h6a1 1 0 0 1 1 1v10a1 1 0 0 1-1 1H3a1 1 0 0 1-1-1V1a1 1 0 0 1 1-1zm0.5 1.5v8h5v-8z"/></svg>
        555-318-40267
      </li>
      <li class="contact__item">
        <svg class="contact__icon" viewBox="0 0 12 12"><path d="M6 1l6 4v6H0V5zM1.5 5.4L6 8.4l4.5-3L6 2.6z"/></svg>
        info@corvanagroup.com
      </li>
      <li class="contact__item">
        <svg class="contact__icon" viewBox="0 0 12 12"><circle cx="6" cy="6" r="5.5"/></svg>
        www.corvanagroup.com
      </li>
    </ul>
    <address class="address">P.O. Box&nbsp; Street Name<br>Country Name AB, A5B 521</address>
  </section>

  <section class="card card--back">
    <div class="brand">
      <span class="brand__mark"></span>
      <span class="brand__name">Corvana Group</span>
    </div>
    <div class="site">www.<strong>corvanagroup</strong>.com</div>
  </section>
</body>
</html>
```